Employees at T&M Gale Power Solutions need new modern business cards

We need new business cards that showcase our new rebranded logo. We are seeking modern, clean, fresh, attractive cards while still being professional. We want to stand out. A little bit about us: we work in Canada and the USA. We offer Technical Field Advisors to support wind turbine manufacturers through the construction phase of wind farms. I am attaching a mock inspiration picture to lead you in the direction we want to see this go. Also, FYI We have approx. 10/11 different employees that would need their own card. Let me know when you would need everyone's name. We would love to see some black and white options as well as color copies- when using colors we want green to be the dominant color with accents for blue and orange (colors should match our logo). I have also attached copies of our old business card for reference.

Contact Information for Business Card

Name, Telephone, Email, address, company name, website. EXAMPLE: Hugh Marlow, HughMarlow@tandmgale.example, 555-381-4926, 217763 Birch Line #9, Elmhurst, ON X1Y 2Z3, www.tandmgale.example

Colors
0054AA
0677BA
7BADD7
CADEEF
E8F1F8
00AB8E
00BBA5
67D7C9
C6EFE9
E9F9F6
F0912C
F2A743
F7CA91
FBE8D2
FDF5EE

Requirements
Must have
• 2 sided business card

```html
<!DOCTYPE html>
<html lang="en">
<head>
<meta charset="utf-8">
<title>T&amp;M Gale Power Solutions — Business Card</title>
<link rel="stylesheet" href="https://fonts.googleapis.com/css2?family=Arimo:wght@400;700&display=swap">
<style>
  :root {
    --bg: #e4e4e2;
    --paper: #ffffff;
    --green: #33ad3f;
    --blue: #0677ba;
    --blue-deep: #0562a3;
    --blue-light: #1a9ad8;
    --orange: #f29a1f;
    --text: #555a5f;
    --watermark: #ececec;
    --white: #ffffff;
  }
  * { box-sizing: border-box; margin: 0; padding: 0; }
  html, body { width: 1200px; height: 801px; overflow: hidden; }
  body {
    background: var(--bg);
    font-family: "Arimo", Arial, sans-serif;
    position: relative;
  }
  .card {
    position: absolute;
    width: 520px;
    height: 300px;
    box-shadow: 0 6px 18px rgba(0,0,0,.18);
    overflow: hidden;
  }

  /* Front side */
  .card-front { left: 50px; top: 150px; background: var(--paper); }
  .watermark-area {
    position: absolute; right: 40px; top: 10px;
    width: 250px; height: 250px; border-radius: 50%;
    background: var(--watermark);
  }
  .brand {
    position: absolute; left: 34px; top: 36px;
    display: flex; align-items: center; gap: 10px;
  }
  .brand-dot { width: 38px; height: 38px; border-radius: 50%; background: var(--green); }
  .brand-name {
    color: var(--green); font-weight: 700; font-size: 19px;
    line-height: 1.05; letter-spacing: .5px; text-transform: uppercase;
  }
  .person-name {
    position: absolute; left: 34px; top: 138px;
    color: var(--orange); font-weight: 700; font-size: 25px;
    letter-spacing: .5px; text-transform: uppercase;
  }
  .contact-list {
    position: absolute; left: 34px; top: 182px;
    list-style: none; color: var(--text); font-size: 13px;
  }
  .contact-list li { display: flex; align-items: center; gap: 9px; height: 21px; }
  .contact-list svg { width: 12px; height: 12px; fill: var(--orange); flex: none; }
  .address {
    position: absolute; right: 30px; bottom: 38px;
    color: var(--text); font-size: 13px; line-height: 1.45; text-align: right;
  }
  .edge-stripe { position: absolute; left: 0; right: 0; bottom: 0; height: 10px; display: flex; }
  .edge-stripe .seg-orange { flex: 40; background: var(--orange); }
  .edge-stripe .seg-blue { flex: 30; background: var(--blue); }
  .edge-stripe .seg-green { flex: 30; background: var(--green); }
  .side-tab {
    position: absolute; left: 0; bottom: 34px; width: 7px; height: 22px;
    background: var(--orange); border-radius: 0 3px 3px 0;
  }

  /* Back side */
  .card-back {
    left: 630px; top: 350px;
    background: linear-gradient(135deg, var(--blue-light) 0%, var(--blue) 55%, var(--blue-deep) 100%);
  }
  .pattern-area { position: absolute; inset: 0; }
  .back-brand {
    position: absolute; right: 34px; bottom: 44px;
    display: flex; align-items: center; gap: 12px;
  }
  .back-brand .brand-dot { background: var(--white); width: 44px; height: 44px; }
  .back-brand .brand-name { color: var(--white); font-size: 21px; }
</style>
</head>
<body>

<section class="card card-front" aria-label="Business card front">
  <div class="watermark-area" role="img" aria-label="Faint large brand mark decoration"></div>

  <div class="brand">
    <span class="brand-dot"></span>
    <div class="brand-name">T&amp;M Gale<br>Power Solutions</div>
  </div>

  <h1 class="person-name">Hugh Marlow</h1>

  <ul class="contact-list">
    <li>
      <svg viewBox="0 0 24 24" aria-hidden="true"><path d="M6.6 10.8a15.1 15.1 0 0 0 6.6 6.6l2.2-2.2a1 1 0 0 1 1-.25 11.4 11.4 0 0 0 3.6.57 1 1 0 0 1 1 1V20a1 1 0 0 1-1 1A17 17 0 0 1 3 4a1 1 0 0 1 1-1h3.5a1 1 0 0 1 1 1c0 1.25.2 2.45.57 3.6a1 1 0 0 1-.25 1z"/></svg>
      555-381-4926
    </li>
    <li>
      <svg viewBox="0 0 24 24" aria-hidden="true"><path d="M2 5h20v14H2z M2 5l10 8 10-8" stroke="#fff" stroke-width="1.5"/></svg>
      HughMarlow@tandmgale.example
    </li>
    <li>
      <svg viewBox="0 0 24 24" aria-hidden="true"><circle cx="12" cy="12" r="10"/><path d="M2 12h20M12 2c3 3 3 17 0 20M12 2c-3 3-3 17 0 20" stroke="#fff" stroke-width="1.5" fill="none"/></svg>
      www.tandmgale.example
    </li>
  </ul>

  <address class="address" style="font-style:normal">
    217763 Birch Line #9<br>Elmhurst, ON X1Y 2Z3
  </address>

  <span class="side-tab"></span>
  <div class="edge-stripe">
    <span class="seg-orange"></span><span class="seg-blue"></span><span class="seg-green"></span>
  </div>
</section>

<section class="card card-back" aria-label="Business card back">
  <div class="pattern-area" role="img" aria-label="Embossed repeating brand pattern on blue"></div>
  <div class="back-brand">
    <span class="brand-dot"></span>
    <div class="brand-name">T&amp;M Gale<br>Power Solutions</div>
  </div>
</section>

</body>
</html>
```